Oil and Gas Industry training School Needs a Web Design

We need a web design for a new company based in Northern British Columbia Canada called "SKILLPATH Trade Academy Inc." Is a training facility that specializes in different aspects of Pipeline Construction training. We also offer compliance courses for Oil and Gas Industry. We would like to see designs that us the colours in our logo.

Target Market(s)

Is Men and women between 18-60 that want to work in the oil and gas industry

Industry/Entity Type

School

Number of Pages Required

5+ page

Font styles to use
Sans Serif

Colors
f37022
000000
333333
ffffff
848484
7f7f7f
c8c8c8
f68d4d
fee3d4

Requirements
Must have
• a easy back end for editing content! and adding additional pages if necessary.

```html
<!DOCTYPE html>
<html lang="en">
<head>
<meta charset="utf-8">
<title>SKILLPATH Trade Academy Inc.</title>
<link href="https://fonts.googleapis.com/css2?family=Open+Sans:wght@300;400;600;700&display=swap" rel="stylesheet">
<style>
:root{
  --orange:#f37022;
  --orange-light:#f68d4d;
  --orange-pale:#fee3d4;
  --black:#000000;
  --dark:#333333;
  --grey:#848484;
  --grey-mid:#7f7f7f;
  --grey-light:#c8c8c8;
  --white:#ffffff;
  --band:#eeeeee;
  --soft:#f7f7f7;
}
*{margin:0;padding:0;box-sizing:border-box}
html,body{width:954px;height:1200px;overflow:hidden;background:var(--white);font-family:"Open Sans",sans-serif;color:var(--dark)}
.page{position:relative;width:954px;height:1200px}

.site-header{position:absolute;top:0;left:0;width:954px;height:112px}
.brand{position:absolute;left:136px;top:24px;display:flex;align-items:center;gap:14px}
.brand-dot{width:66px;height:66px;border-radius:50%;background:var(--dark)}
.brand-name{font-size:30px;font-weight:700;color:var(--dark);letter-spacing:-.5px;line-height:1}
.brand-name small{display:block;font-size:14px;font-weight:700;letter-spacing:.5px;margin-top:6px}
.header-right{position:absolute;right:134px;top:34px;text-align:right}
.social{display:flex;justify-content:flex-end;gap:8px;margin-bottom:6px}
.social span{width:24px;height:24px;border-radius:50%;background:var(--grey-light)}
.social span:nth-child(2){background:var(--dark)}
.tel{font-size:20px;font-weight:400;color:var(--black)}
.tel b{color:var(--orange);font-weight:400}

.main-nav{position:absolute;top:112px;left:0;width:954px;height:45px;background:var(--band)}
.main-nav ul{list-style:none;position:absolute;left:136px;top:0;height:45px;display:flex;align-items:center}
.main-nav li{font-size:12.5px;font-weight:600;color:var(--dark);margin-right:49px}
.main-nav .home{width:53px;height:45px;background:var(--white);border-bottom:3px solid var(--orange);margin-right:29px;display:flex;align-items:center;justify-content:center}

.hero{position:absolute;top:157px;left:0;width:954px;height:316px;background:linear-gradient(160deg,#8a8a6a 0%,#b99a86 35%,#9c8f8a 60%,#c9d4e0 100%)}
.hero-title{position:absolute;top:94px;width:100%;text-align:center;font-size:33px;font-weight:600;color:var(--white);text-shadow:0 1px 3px rgba(0,0,0,.5)}
.hero-text{position:absolute;top:146px;left:176px;width:602px;text-align:center;font-size:12.5px;line-height:15px;color:var(--white);text-shadow:0 1px 2px rgba(0,0,0,.6)}
.hero-btn{position:absolute;top:228px;left:378px;width:198px;height:33px;border:1px solid var(--orange);color:var(--orange);font-size:12.5px;font-weight:600;display:flex;align-items:center;justify-content:center}
.slider-dots{position:absolute;top:290px;left:452px;display:flex;gap:2px}
.slider-dots span{width:8px;height:8px;background:var(--dark)}
.slider-dots .active{background:var(--orange)}

.services{position:absolute;top:496px;left:136px;width:682px;height:140px;display:flex}
.service{width:226px;height:140px;text-align:center;padding-top:18px}
.service.active{background:var(--soft)}
.service-icon{width:82px;height:82px;border-radius:50%;background:var(--dark);margin:0 auto 14px}
.service h3{font-size:12.5px;font-weight:600;color:var(--black)}
.rule{position:absolute;top:659px;left:136px;width:682px;height:1px;background:#e6e6e6}

.welcome{position:absolute;top:690px;left:0;width:954px;text-align:center}
.welcome h2{font-size:25px;font-weight:600;color:var(--orange);display:flex;align-items:center;justify-content:center;gap:16px}
.welcome h2::before,.welcome h2::after{content:"";width:222px;height:1px;background:#e6e6e6}
.welcome p{font-size:10px;font-weight:300;line-height:12px;color:var(--grey);width:650px;margin:6px auto 0}
.welcome p+p{margin-top:11px}

.news{position:absolute;top:816px;left:0;width:954px;height:207px;background:var(--soft)}
.news h2{text-align:center;font-size:23px;font-weight:400;color:var(--grey-mid);margin-top:26px}
.news-grid{position:absolute;top:65px;left:144px;display:flex;gap:8px}
.news-item{width:215px;height:126px;position:relative}
.news-item.one{background:linear-gradient(120deg,#d9dde3,#b7c3cf)}
.news-item.two{background:var(--orange-light);color:var(--white);text-align:center;padding-top:20px}
.news-item.three{background:linear-gradient(120deg,#7c8a9e,#c3ccd6)}
.news-item.two h4{font-size:12px;font-weight:600;margin-top:4px}
.news-item.two p{font-size:8.5px;line-height:10px;margin:4px 12px 0}

.site-footer{position:absolute;top:1023px;left:0;width:954px;text-align:center}
.foot-brand{display:flex;align-items:center;justify-content:center;gap:6px;margin-top:16px}
.foot-brand .dot{width:24px;height:24px;border-radius:50%;background:var(--dark)}
.foot-brand b{font-size:16px;font-weight:700;color:var(--dark)}
.foot-brand small{display:block;font-size:8px;font-weight:700}
.copyright{font-size:8px;color:var(--dark);margin-top:10px;letter-spacing:.2px}
.site-footer .social{justify-content:center;margin-top:8px}
.bottom-bar{position:absolute;top:1166px;left:0;width:954px;height:34px;background:var(--orange)}
</style>
</head>
<body>
<div class="page">
  <header class="site-header">
    <div class="brand">
      <span class="brand-dot"></span>
      <div class="brand-name">SKILLPATH<small>TRADE ACADEMY INC.</small></div>
    </div>
    <div class="header-right">
      <div class="social"><span></span><span></span><span></span></div>
      <div class="tel"><b>TEL:</b> 12 34 56 78 90</div>
    </div>
  </header>

  <nav class="main-nav">
    <ul>
      <li class="home"><svg width="20" height="18" viewBox="0 0 20 18"><path d="M10 1 1 9h3v8h12V9h3z" fill="#f37022"/></svg></li>
      <li>COURSE OFFERINGS</li>
      <li>LEARNING PROGRAMS</li>
      <li>ABOUT US</li>
      <li>NEWS</li>
      <li>CONTACT US</li>
    </ul>
  </nav>

  <section class="hero" role="img" aria-label="Photo of industrial pipelines and storage tanks on a grassy field">
    <h1 class="hero-title">LOREM IPSUM DOLOR SIT AMET</h1>
    <p class="hero-text">Lorem ipsum dolor sit amet, consectetuer adipiscing elit, sed diam nonummy nibh euismod tincidunt ut laoreet dolore magna aliquam erat volutpat. Ut wisi enim ad minim veniam, quis nostrud exerci tation ullamcorper suscipit lobortis nisl ut aliquip ex ea commodo consequat.</p>
    <div class="hero-btn">START LEARNING</div>
    <div class="slider-dots"><span></span><span></span><span></span><span></span><span class="active"></span><span></span></div>
  </section>

  <section class="services">
    <div class="service">
      <div class="service-icon" role="img" aria-label="Gear icon with pipeline valve"></div>
      <h3>PIPELINE CONSTRUCTION TRAINING</h3>
    </div>
    <div class="service active">
      <div class="service-icon" role="img" aria-label="Gear icon with oil derrick"></div>
      <h3>OIL INDUSTRY TRAINING</h3>
    </div>
    <div class="service">
      <div class="service-icon" role="img" aria-label="Gear icon with gas flare rig"></div>
      <h3>GAS INDUSTRY TRAINING</h3>
    </div>
  </section>
  <div class="rule"></div>

  <section class="welcome">
    <h2>WELCOME</h2>
    <p>Lorem ipsum dolor sit amet, consectetuer adipiscing elit, sed diam nonummy nibh euismod tincidunt ut laoreet dolore magna aliquam erat volutpat. Ut wisi enim ad minim veniam, quis nostrud exerci tation ullamcorper suscipit lobortis nisl ut aliquip ex ea commodo consequat.</p>
    <p>Duis autem vel eum iriure dolor in hendrerit in vulputate velit esse molestie consequat, vel illum dolore eu feugiat nulla facilisis at vero eros et accumsan et iusto odio dignissim qui blandit praesent luptatum zzril delenit augue duis dolore te feugait nulla facilisi.</p>
  </section>

  <section class="news">
    <h2>LATEST NEWS</h2>
    <div class="news-grid">
      <div class="news-item one" role="img" aria-label="Photo of students seated in a classroom"></div>
      <div class="news-item two" role="img" aria-label="Photo of a surveyor with a level instrument, under an orange overlay">
        <svg width="34" height="34" viewBox="0 0 34 34" fill="none" stroke="#fff" stroke-width="2"><circle cx="14" cy="14" r="11"/><path d="M22 22l10 10M14 8v12M8 14h12"/></svg>
        <h4>Lorem ipsum dolor</h4>
        <p>Consectetuer adipiscing elit, sed diam nonummy nibh euismod tincidunt ut laoreet dolore magna aliquam erat volutpat.</p>
      </div>
      <div class="news-item three" role="img" aria-label="Photo of two workers in hard hats at a refinery"></div>
    </div>
  </section>

  <footer class="site-footer">
    <div class="foot-brand"><span class="dot"></span><b>SKILLPATH<small>TRADE ACADEMY INC.</small></b></div>
    <p class="copyright">COPYRIGHT © 2014 SKILLPATH TRADE ACADEMY INC.</p>
    <div class="social"><span></span><span></span><span></span></div>
  </footer>
  <div class="bottom-bar"></div>
</div>
</body>
</html>
```